Poster design for a vet clinic

Running a campaign called 'Tail teller', which is where people get a $30 voucher for themselves and their friend if they refer somebody to our vet clinic.

Text something like:
We love Tail Tellers!
Refer a fur friend to our friendly team and both your fur child and their fur child will receive a $30 voucher to use in clinic! *
* Limited to one pet per fur parent and the referred fur parent must be new to our clinic. Unlimited vouchers for number of referrals!

I want it to be cute but professional. You can see the design styles at mossbury-vet.com.au/kelvale and see the logo there too.
I am thinking of having a dog whispering to a cat or something like that as the main image.
I would like both the photoshop file and the pdf please. Would be for an A2 poster.

```html
<!DOCTYPE html>
<html lang="en">
<head>
<meta charset="utf-8">
<title>We Love Tail Tellers! – Mossbury Veterinary Clinic Kelvale</title>
<link rel="stylesheet" href="https://fonts.googleapis.com/css2?family=Roboto:ital,wght@0,300;0,400;0,700;0,900;1,700;1,900&family=Roboto+Condensed:ital,wght@0,700;1,300;1,400;1,700&display=swap">
<style>
  :root {
    --brown: #5c3916;
    --orange: #f5901e;
    --ink-grey: #4b4b4b;
    --bar-grey: #555555;
    --text-grey: #5a5a5a;
    --paper: #ffffff;
    --art-light: #e6edf9;
    --art-blue: #4f73cf;
  }
  * { margin: 0; padding: 0; box-sizing: border-box; }
  html, body { width: 852px; height: 1200px; overflow: hidden; background: var(--brown); }
  .poster {
    position: relative;
    width: 852px; height: 1200px;
    background: var(--brown);
    font-family: "Roboto", Arial, sans-serif;
  }
  .poster-sheet {
    position: absolute;
    left: 22px; top: 22px; right: 22px; bottom: 22px;
    background: var(--paper);
  }
  .clinic-mark {
    position: absolute; left: 0; right: 0; top: 42px;
    text-align: center;
  }
  .clinic-name {
    font-weight: 700; font-size: 54px; line-height: 1;
    color: var(--brown); letter-spacing: -1px;
  }
  .clinic-type {
    margin-top: 8px;
    font-weight: 700; font-size: 11px; letter-spacing: 2.5px;
    color: var(--brown);
  }
  .clinic-rule {
    width: 196px; height: 1px; margin: 4px auto 0;
    background: var(--orange);
  }
  .clinic-location {
    margin-top: 5px;
    font-weight: 400; font-size: 20px; color: var(--orange);
  }
  .headline-we {
    position: absolute; left: 393px; top: 195px;
    width: 78px; height: 78px; border-radius: 50%;
    background: var(--brown); color: var(--paper);
    font-weight: 900; font-size: 38px; line-height: 78px; text-align: center;
    z-index: 1;
  }
  .headline-love {
    position: absolute; left: 0; right: 0; top: 240px;
    text-align: center;
    font-weight: 900; font-size: 104px; line-height: 1;
    color: var(--orange); letter-spacing: -2px;
    z-index: 2;
  }
  .headline-tellers {
    position: absolute; left: 0; right: 0; top: 306px;
    text-align: center;
    font-weight: 900; font-size: 146px; line-height: 1;
    color: var(--brown); letter-spacing: -3px;
  }
  .headline-tellers .bang { font-size: 60px; font-weight: 400; letter-spacing: 0; }
  .hero-art {
    position: absolute; left: 150px; top: 452px;
    width: 560px; height: 300px;
    background: linear-gradient(180deg, var(--art-light) 0%, var(--art-blue) 100%);
  }
  .refer-lines {
    position: absolute; left: 0; right: 0; top: 764px;
    text-align: center;
    font-family: "Roboto Condensed", Arial, sans-serif;
    font-weight: 700; font-size: 23px; line-height: 27px; color: var(--paper);
    letter-spacing: -0.3px;
  }
  .refer-lines span { background: var(--bar-grey); padding: 0 3px; }
  .receive-line {
    position: absolute; left: 0; right: 0; top: 826px;
    text-align: center;
    font-family: "Roboto Condensed", Arial, sans-serif;
    font-style: italic; font-weight: 300; font-size: 28px; color: var(--ink-grey);
  }
  .voucher-amount {
    position: absolute; left: 252px; top: 862px;
    width: 330px; height: 180px;
  }
  .voucher-amount text {
    font-family: "Roboto", Arial, sans-serif;
    font-style: italic; font-weight: 900;
    fill: var(--orange); stroke: var(--brown);
    paint-order: stroke; stroke-linejoin: round;
  }
  .voucher-use {
    position: absolute; left: 0; right: 0; top: 1044px;
    text-align: center;
  }
  .voucher-use span {
    display: inline-block; background: var(--bar-grey); color: var(--paper);
    font-family: "Roboto Condensed", Arial, sans-serif;
    font-style: italic; font-weight: 400; font-size: 29px; line-height: 29px;
    padding: 0 6px;
  }
  .terms {
    position: absolute; left: 0; right: 0; top: 1098px;
    text-align: center;
    font-weight: 300; font-size: 26px; line-height: 31px; color: var(--text-grey);
    letter-spacing: -0.3px;
  }
</style>
</head>
<body>
<main class="poster">
  <div class="poster-sheet"></div>

  <header class="clinic-mark">
    <div class="clinic-name">Mossbury</div>
    <div class="clinic-type">VETERINARY CLINIC</div>
    <div class="clinic-rule"></div>
    <div class="clinic-location">KELVALE</div>
  </header>

  <h1>
    <span class="headline-we">We</span>
    <span class="headline-love">Love Tail</span>
    <span class="headline-tellers">Tellers<span class="bang">!</span></span>
  </h1>

  <div class="hero-art" role="img" aria-label="Watercolour illustration of a white kitten and puppy nuzzling, on a blue and pink paint splash"></div>

  <p class="refer-lines">
    <span>Refer a fur friend to our friendly team</span><br>
    <span>and both your fur child &amp;</span>
  </p>

  <p class="receive-line">Their fur child will receive a</p>

  <svg class="voucher-amount" viewBox="0 0 330 180" aria-label="$30">
    <text x="6" y="130" font-size="92" stroke-width="7">$</text>
    <text x="66" y="170" font-size="218" stroke-width="10" letter-spacing="-8">30</text>
  </svg>

  <p class="voucher-use"><span>Voucher to use in clinic!</span></p>

  <p class="terms">Limited to one pet per fur parent and the referred fur parent must be<br>new to our clinic. Unlimited vouchers for number of referrals!</p>
</main>
</body>
</html>
```